Please make an eye catching and elegant flyer. Here is the content
Lorena's 70th Birthday Bash
Friday September 13th, 2024
8pm - 12midnight
Location:
Pelbrook's Oakland
47 Marlow St, Oakland, CA 94618
For more information and to RSVP contact 916-482-3157 or 510-647-2083

Colors
FFF300
FFF600
FEFA6F
FFFEC7
FFFEE8
EB3D1F
EC4F4E
F09395
F8D3D4
FCEDEE
A7469A
B969AE
D3A5CF
EDDBEB
F8F0F9

Requirements
Nice to have
• Her favorite colors are royal purple, white, red. and gold. You don't have to use all of these colors yet at least a couple would be nice.

```html
<!DOCTYPE html>
<html lang="en">
<head>
<meta charset="utf-8">
<title>Lorena's 70th Birthday Bash</title>
<link href="https://fonts.googleapis.com/css2?family=Bebas+Neue&family=Montserrat:wght@500;600;700;800&family=Mrs+Saint+Delafield&display=swap" rel="stylesheet">
<style>
:root{
  --stage:#f4f2f5;
  --purple-deep:#1f0a45;
  --purple-mid:#3a1475;
  --purple-bright:#5a22a6;
  --gold:#f2c21a;
  --gold-light:#fff300;
  --white:#ffffff;
  --fabric-green:#1f9e58;
  --fabric-orange:#eb8a1f;
  --fabric-red:#eb3d1f;
}
*{margin:0;padding:0;box-sizing:border-box}
html,body{width:1200px;height:684px;overflow:hidden;background:var(--stage)}
.stage{position:relative;width:1200px;height:684px;display:flex;align-items:center;justify-content:center}
.flyer{position:relative;width:456px;height:644px;overflow:hidden;
  background:
    linear-gradient(160deg,transparent 38%,rgba(140,80,220,.35) 46%,transparent 54%),
    linear-gradient(200deg,transparent 55%,rgba(120,60,200,.3) 63%,transparent 72%),
    linear-gradient(180deg,var(--purple-deep) 0%,var(--purple-mid) 55%,var(--purple-bright) 100%);
  font-family:'Montserrat',sans-serif;color:var(--white)}
.portrait{position:absolute;left:192px;top:36px;width:264px;height:608px;
  border-radius:120px 120px 0 0;
  background:
    radial-gradient(ellipse at 45% 22%,rgba(120,70,40,.9) 0%,rgba(120,70,40,0) 32%),
    linear-gradient(160deg,var(--fabric-green) 0%,var(--fabric-orange) 40%,var(--fabric-green) 70%,var(--fabric-orange) 100%);
  opacity:.92}
.glow-ring{position:absolute;left:0;top:0;width:456px;height:644px;pointer-events:none}
.title{position:absolute;left:31px;top:40px;font-family:'Bebas Neue',sans-serif;line-height:.86}
.title-name{display:block;font-size:70px;color:var(--gold);letter-spacing:-1px}
.title-age{display:block;font-size:118px;color:var(--white);letter-spacing:-2px;margin-top:-4px}
.title-event{display:block;font-size:58px;color:var(--gold);letter-spacing:-1px;margin-top:-2px}
.title-script{position:absolute;left:50px;top:186px;font-family:'Mrs Saint Delafield',cursive;font-size:92px;color:var(--white);line-height:1}
.details{position:absolute;left:33px;top:322px;width:170px}
.date{font-size:21px;font-weight:600;line-height:23px;letter-spacing:.3px}
.date strong{font-weight:800}
.time{margin-top:6px;font-size:14px;font-weight:800;color:var(--gold)}
.rule{width:16px;height:1.5px;background:var(--white);margin:10px 0 12px}
.label{font-size:8px;font-weight:800;color:var(--gold);letter-spacing:.3px}
.info{font-size:8px;font-weight:500;line-height:10px;text-transform:uppercase;white-space:nowrap}
.info strong{font-weight:800}
.venue{margin-top:2px}
.contact{margin-top:11px}
.gallery{position:absolute;left:33px;top:526px;display:flex}
.gallery-item{width:81px;height:81px;border-radius:50%;border:2px solid #7a5aa8;margin-right:-6px}
.gallery-item.portrait-red{background:radial-gradient(circle at 50% 40%,#6a2a20,#1a0a0a 70%)}
.gallery-item.group{background:linear-gradient(160deg,#c9a27a,#8a4f3a 60%,#d9b48f)}
.gallery-item.stage-scene{background:linear-gradient(170deg,#b7a9b8,#d08a5a 55%,#8f6f8a)}
</style>
</head>
<body>
<div class="stage">
  <article class="flyer">
    <div class="portrait" role="img" aria-label="Photo of the guest of honour dancing with raised hands in a green and orange patterned dress"></div>
    <svg class="glow-ring" viewBox="0 0 456 644" aria-hidden="true">
      <defs>
        <filter id="ring-glow" x="-20%" y="-50%" width="140%" height="200%">
          <feGaussianBlur stdDeviation="3" result="b"/>
          <feMerge><feMergeNode in="b"/><feMergeNode in="b"/><feMergeNode in="SourceGraphic"/></feMerge>
        </filter>
      </defs>
      <path d="M140 520 C 240 490, 420 450, 428 400 C 432 370, 400 365, 380 372" fill="none" stroke="#fff6a8" stroke-width="2.5" filter="url(#ring-glow)"/>
      <path d="M126 618 C 115 600, 160 585, 240 575 C 320 565, 400 560, 420 548" fill="none" stroke="#fff6a8" stroke-width="2.5" filter="url(#ring-glow)"/>
      <path d="M280 270 C 330 250, 400 220, 456 205" fill="none" stroke="rgba(255,255,255,.55)" stroke-width="1.2"/>
    </svg>
    <h1 class="title">
      <span class="title-name">LORENA'S</span>
      <span class="title-age">70TH</span>
      <span class="title-event">BIRTHDAY</span>
    </h1>
    <span class="title-script">Bash</span>
    <section class="details">
      <p class="date">FRIDAY<br>SEPTEMBER<br><strong>13TH, 2024</strong></p>
      <p class="time">8PM - 12MIDNIGHT</p>
      <div class="rule"></div>
      <p class="label">LOCATION:</p>
      <p class="info venue">Pelbrook's Oakland<br>47 Marlow St, Oakland, CA 94618</p>
      <p class="info contact">For more information and to<br><strong>RSVP</strong> contact 916-482-3157<br>or 510-647-2083</p>
    </section>
    <div class="gallery">
      <div class="gallery-item portrait-red" role="img" aria-label="Photo of the guest of honour in a red outfit and head wrap"></div>
      <div class="gallery-item group" role="img" aria-label="Photo of a group of dancers in traditional costume"></div>
      <div class="gallery-item stage-scene" role="img" aria-label="Photo of a performer in orange dancing on stage"></div>
    </div>
  </article>
</div>
</body>
</html>
```